Home Page Design

We are refreshing our website and need someone to design a very clean modern home page. We have a wireframe for the content and basic layout (see attached). We just need someone to make it look beautiful.

This web page will be hosted on a private server using HTML5. I have developers who will integrate the rotating images and referenced video files - we just need you to focus on the visual elements.

You can take a look at our current website at tarnivoxel.com for color style guides, logos, etc.

```html
<!DOCTYPE html>
<html lang="en">
<head>
<meta charset="utf-8">
<title>Tarnivoxel – Home</title>
<link href="https://fonts.googleapis.com/css2?family=Roboto:wght@300;400;500&display=swap" rel="stylesheet">
<style>
:root{
  --brand-blue:#2b5eae;
  --accent-green:#7ccd3c;
  --stat-orange:#f6a21d;
  --ink:#222;
  --muted:#555;
  --white:#fff;
}
*{margin:0;padding:0;box-sizing:border-box}
html,body{width:1200px;height:1200px;overflow:hidden;background:var(--white)}
body{font-family:"Roboto",Helvetica,Arial,sans-serif;color:var(--ink);position:relative}
.abs{position:absolute}
.utility-bar{left:0;top:0;width:1200px;height:22px;background:var(--brand-blue);color:var(--white);font-size:12px}
.utility-bar a{position:absolute;top:4px;color:var(--white);text-decoration:none}
.utility-phone{position:absolute;right:40px;top:4px;display:flex;align-items:center;gap:6px}
.site-header{left:0;top:22px;width:1200px;height:71px;background:var(--white)}
.brand{position:absolute;left:26px;top:26px;display:flex;align-items:center;gap:6px;font-size:22px;font-weight:400;color:var(--brand-blue)}
.brand-dot{width:12px;height:12px;border-radius:50%;background:var(--brand-blue)}
.main-nav a{position:absolute;top:38px;font-size:12px;color:#444;text-decoration:none}
.main-nav a.active{color:var(--accent-green);text-decoration:underline}
.header-cta{position:absolute;top:34px;font-size:12.5px;color:#444;display:flex;align-items:center;gap:5px}
.hero-media{left:0;top:93px;width:880px;height:474px;background:linear-gradient(120deg,#3c3c3c 0%,#6b6b6b 40%,#9a9a9a 70%,#7d7d7d 100%)}
.hero-copy{left:0;top:93px;width:880px;height:474px;color:var(--white);text-align:center}
.hero-title{position:absolute;left:0;width:880px;top:180px;font-size:38px;font-weight:400;line-height:45px}
.btn{position:absolute;background:var(--accent-green);color:var(--white);font-size:13px;border-radius:3px;display:flex;align-items:center;justify-content:center}
.hero-tagline{position:absolute;left:0;width:880px;top:424px;font-size:15px}
.stat{left:882px;width:318px;background:var(--brand-blue);color:var(--white);text-align:center}
.stat > div{position:absolute;left:0;width:318px}
.stat-label{font-size:30px;font-weight:300;line-height:36px}
.stat-value{font-size:66px;font-weight:300;color:var(--stat-orange);line-height:66px}
.stat-note{font-size:22px;font-weight:300;line-height:28px}
.monitor{left:90px;top:654px;width:434px;height:348px;background:linear-gradient(#2a2a2a,#1a1a1a);border-radius:4px}
.feature-title{left:708px;top:656px;font-size:32px;font-weight:300}
.feature-list{left:704px;top:710px;list-style:none;font-size:14.5px;font-weight:300;color:#333}
.feature-list li{height:27.5px}
.feature-list li::before{content:"· ";font-weight:500}
.band{left:0;top:1086px;width:1200px;height:114px;background:var(--brand-blue)}
.band-title{left:136px;top:1178px;font-size:32px;font-weight:300;color:var(--white)}
.band-media{left:618px;top:1187px;width:496px;height:13px;background:linear-gradient(90deg,#c9b9a4,#8f7d6b)}
</style>
</head>
<body>
<div class="abs utility-bar">
  <a style="left:34px">About Us</a>
  <a style="left:106px">Contact</a>
  <a style="left:174px">Support</a>
  <a style="left:242px">Partners</a>
  <div class="utility-phone">
    <svg width="11" height="11" viewBox="0 0 24 24"><path fill="#fff" d="M6.6 10.8a15 15 0 0 0 6.6 6.6l2.2-2.2a1 1 0 0 1 1-.25 11.4 11.4 0 0 0 3.6.57 1 1 0 0 1 1 1V20a1 1 0 0 1-1 1A17 17 0 0 1 3 4a1 1 0 0 1 1-1h3.5a1 1 0 0 1 1 1c0 1.25.2 2.45.57 3.570a1 1 0 0 1-.25 1z"/></svg>
    800 555 0142
  </div>
</div>

<header class="abs site-header">
  <div class="brand"><span class="brand-dot"></span>tarnivoxel</div>
  <nav class="main-nav">
    <a class="active" style="left:179px">Home</a>
    <a style="left:246px">Solutions</a>
    <a style="left:328px">Pricing</a>
    <a style="left:410px">FAQ</a>
  </nav>
  <div class="header-cta" style="left:988px">Free Assessment
    <svg width="10" height="12" viewBox="0 0 10 12"><path d="M2 1l6 5-6 5" fill="none" stroke="#2b8fe0" stroke-width="2.5"/></svg></div>
  <div class="header-cta" style="left:1121px">Login
    <svg width="10" height="12" viewBox="0 0 10 12"><path d="M2 1l6 5-6 5" fill="none" stroke="#2b8fe0" stroke-width="2.5"/></svg></div>
</header>

<div class="abs hero-media" role="img" aria-label="Hand holding a phone in front of a screen showing web traffic analytics charts"></div>
<section class="abs hero-copy">
  <h1 class="hero-title">The Ultimate Velora<br>Cost Optimization Solution</h1>
  <div class="btn" style="left:364px;top:301px;width:130px;height:36px">What We Do</div>
  <p class="hero-tagline">NextGen Technology • Advanced Cost Analytics • Managed Services • Certified Velora Engineers</p>
</section>

<div class="abs stat" style="top:93px;height:235px">
  <div class="stat-label" style="top:41px">Average Reduction</div>
  <div class="stat-value" style="top:94px">47%</div>
  <div class="stat-note" style="top:175px">Total Velora Spend</div>
</div>
<div class="abs stat" style="top:330px;height:237px">
  <div class="stat-label" style="top:41px">Average Cash ROI</div>
  <div class="stat-value" style="top:79px">5.1x</div>
  <div class="stat-note" style="top:157px">First Year</div>
</div>

<div class="abs monitor" role="img" aria-label="Desktop monitor displaying the resource scheduling dashboard"></div>
<h2 class="abs feature-title">Advanced Cost Analytics</h2>
<ul class="abs feature-list">
  <li>Access to detailed billing records</li>
  <li>Customizable drill down invoice templates</li>
  <li>Velora tag integration</li>
  <li>Comprehensive invoice variance analysis</li>
  <li>Side by side VX2 pricing comparisons</li>
  <li>VX2 total cost of ownership</li>
  <li>Spending trends</li>
  <li>Cost forecasting</li>
</ul>
<div class="btn" style="left:707px;top:949px;width:130px;height:35px">Learn More</div>

<div class="abs band"></div>
<h2 class="abs band-title">Advanced Cost Analytics</h2>
<div class="abs band-media" role="img" aria-label="Photo of a team working together"></div>
</body>
</html>
```